Purely Windswept needs an eye catching marketing flyer

Our new Luminous Airflow(r) business needs an eye catching marketing flyer. We think A5 sizing?
website link (where you can understand more about breathwork is www.purelywindswept.co.uk)
Design whatever you would like to design some things that could be of use to mention are below. Will leave it in your capable hands.
Logo files for Purely Windswept attached, use whichever one is best for your design, should be the main logo and colour scheme for the flyer, the second logo is that of Luminous Airflow(r) the breath school who's body of work we will be delivering. This can be anywhere on the flyer
Flyer is needed to get people interested in breathwork, the potential benefits for breathing better
We offer 1:1 sessions, workshops, corporate training
The flyer will have an offer code 'OpenGlow' which will give 15% off the bookers first 1:1 session
Flyer should include the following contact details: Maybe a "find out how breathwork can help you today. . . "
Tessa Orchard (South): 07700 318 527
Lorraine Pitt (Midlands): 07700 452 183
facebook: we.are.purelywindswept
instagram: _purelywindswept_

```html
<!DOCTYPE html>
<html lang="en">
<head>
<meta charset="utf-8">
<title>Purely Windswept – Breathwork Flyer</title>
<link rel="stylesheet" href="https://fonts.googleapis.com/css2?family=Montserrat:wght@400;500;600;700;800;900&family=Bebas+Neue&family=Roboto+Condensed:wght@500;700&display=swap">
<style>
  :root {
    --page: #f3f3f3;
    --sky-deep: #1f4fd6;
    --sky-mid: #3f7ff0;
    --sky-light: #b9dff5;
    --ink-dark: #16120f;
    --ink-brown: #3b2a20;
    --cyan: #27c3e0;
    --cyan-bright: #37d4ee;
    --white: #ffffff;
    --pale-cyan: #c9f4fb;
    --violet: #7a4ea8;
    --navy: #0d2547;
  }
  * { box-sizing: border-box; margin: 0; padding: 0; }
  html, body { width: 956px; height: 1200px; overflow: hidden; background: var(--page); }
  body { position: relative; font-family: "Montserrat", sans-serif; color: var(--white); }

  .flyer {
    position: absolute; left: 68px; top: 17px;
    width: 820px; height: 1166px; overflow: hidden;
    background: var(--ink-dark);
    box-shadow: 0 8px 24px rgba(0,0,0,.25);
  }

  .hero-photo {
    position: absolute; left: 0; top: 0; width: 820px; height: 780px;
    background:
      radial-gradient(ellipse 60% 50% at 78% 55%, rgba(230,240,250,.55), rgba(230,240,250,0) 70%),
      linear-gradient(180deg, var(--sky-light) 0%, var(--sky-mid) 18%, var(--sky-deep) 55%, #2b62d8 80%, #3b4b55 100%);
  }
  .band-dark {
    position: absolute; left: 0; top: 763px; width: 820px; height: 403px;
    background: linear-gradient(180deg, #151413 0%, #231b16 45%, var(--ink-brown) 100%);
  }

  .brand {
    position: absolute; left: 70px; top: 188px;
    display: flex; align-items: center; gap: 12px;
  }
  .brand-dot { width: 20px; height: 20px; border-radius: 50%; background: var(--white); }
  .brand-name { font-family: "Montserrat", sans-serif; font-weight: 600; font-size: 34px; color: var(--white); }

  .headline-top {
    position: absolute; left: 38px; top: 306px;
    font-weight: 800; font-size: 54px; letter-spacing: .5px; line-height: 1;
  }
  .headline-main {
    position: absolute; left: 34px; top: 358px;
    font-family: "Bebas Neue", sans-serif; font-size: 154px; line-height: 1; letter-spacing: 1px;
    background: linear-gradient(180deg, var(--white) 20%, var(--pale-cyan) 60%, var(--cyan-bright) 100%);
    -webkit-background-clip: text; background-clip: text; color: transparent;
  }
  .headline-sub {
    position: absolute; left: 38px; top: 496px; width: 443px;
    font-weight: 700; font-size: 33px; line-height: 1; color: var(--pale-cyan);
    border-bottom: 2px solid var(--pale-cyan); padding-bottom: 6px;
  }
  .services {
    position: absolute; left: 38px; top: 546px; width: 443px;
    font-weight: 700; font-size: 16.5px; line-height: 1; color: var(--pale-cyan);
    border-bottom: 2px solid var(--pale-cyan); padding-bottom: 6px;
  }

  .partner-badge {
    position: absolute; left: 40px; top: 600px;
    width: 88px; height: 88px; border-radius: 50%;
    background: radial-gradient(circle, #e9a3c9 0%, var(--violet) 55%, #3c6e56 100%);
  }
  .partner-name {
    position: absolute; left: 30px; top: 694px; width: 108px;
    font-size: 11px; line-height: 1.15; text-align: center; color: #a173d2;
  }
  .science {
    position: absolute; left: 140px; top: 606px; width: 180px;
  }
  .science-title {
    font-family: "Roboto Condensed", sans-serif; font-weight: 700; font-size: 15px;
    padding-bottom: 6px; position: relative;
  }
  .science-title::after {
    content: ""; position: absolute; left: 0; bottom: 0; width: 18px; height: 2px; background: var(--white);
  }
  .science-body { margin-top: 10px; font-size: 12.5px; line-height: 1.33; }

  .offer-intro {
    position: absolute; left: 49px; top: 796px;
    font-weight: 600; font-size: 23px; color: var(--cyan); letter-spacing: .5px; line-height: 1;
  }
  .offer-code {
    position: absolute; left: 47px; top: 824px;
    font-weight: 900; font-size: 56px; line-height: 1; letter-spacing: 1px;
  }
  .offer-value {
    position: absolute; left: 49px; top: 884px; width: 410px;
    font-family: "Bebas Neue", sans-serif; font-size: 52px; line-height: 1;
    border-bottom: 2px solid var(--white); padding-bottom: 2px;
  }
  .offer-terms {
    position: absolute; left: 49px; top: 943px;
    font-weight: 500; font-size: 20px; letter-spacing: .5px; line-height: 1;
  }

  .cta-band {
    position: absolute; left: 0; top: 986px; width: 573px; height: 75px;
    background: var(--cyan); padding: 8px 0 0 49px;
    font-weight: 500; font-size: 27px; line-height: 1.05; letter-spacing: .5px; color: var(--white);
  }
  .cta-band strong { font-weight: 800; color: var(--navy); }

  .side-photo {
    position: absolute; left: 573px; top: 796px; width: 209px; height: 277px;
    background: linear-gradient(160deg, #4a5560 0%, #8b7a66 45%, #d9c7a3 70%, #5d6b78 100%);
  }

  .contact-box {
    position: absolute; left: 49px; top: 1085px; width: 735px; height: 65px;
    border: 1.5px solid var(--white);
    display: flex; align-items: center; padding: 0 14px; gap: 0;
  }
  .social { width: 317px; }
  .social-line { display: flex; align-items: center; gap: 9px; font-weight: 700; font-size: 15px; line-height: 1.6; }
  .social-mark { width: 11px; height: 11px; border-radius: 50%; border: 1.5px solid var(--white); }
  .contact-person { width: 220px; }
  .contact-name { font-family: "Roboto Condensed", sans-serif; font-weight: 500; font-size: 15px; line-height: 1.4; }
  .contact-phone { display: flex; align-items: center; gap: 6px; font-weight: 700; font-size: 19px; line-height: 1.35; }
  .contact-phone svg { width: 14px; height: 14px; }
</style>
</head>
<body>
  <main class="flyer">
    <div class="hero-photo" role="img" aria-label="Woman in white sitting cross-legged in meditation against a soft blue sky with drifting feathers"></div>
    <div class="band-dark"></div>

    <div class="brand">
      <span class="brand-dot"></span>
      <span class="brand-name">Purely Windswept</span>
    </div>

    <h1>
      <span class="headline-top">THE POTENTIAL</span>
      <span class="headline-main">BENEFITS</span>
      <span class="headline-sub">FOR BREATHING BETTER</span>
    </h1>
    <p class="services">We offer 1:1 sessions, workshops, corporate training</p>

    <div class="partner-badge" aria-hidden="true"></div>
    <p class="partner-name">Luminous Airflow®</p>
    <section class="science">
      <h2 class="science-title">THE SCIENCE &amp; RESEARCH</h2>
      <p class="science-body">Luminous Airflow<br>Foundation® are keen to build<br>an evidence base for the<br>breathwork offered<br>to clients.</p>
    </section>

    <p class="offer-intro">THE FLYER WILL HAVE AN OFFER CODE</p>
    <p class="offer-code">'OPENGLOW'</p>
    <p class="offer-value">WHICH WILL GIVE 15% OFF</p>
    <p class="offer-terms">THE BOOKERS FIRST 1:1 SESSION</p>

    <div class="cta-band">FIND OUT HOW <strong>BREATHWORK</strong><br>CAN HELP YOU TODAY</div>

    <div class="side-photo" role="img" aria-label="Woman lying on a cushion with hands resting on her chest during a breathwork session"></div>

    <footer class="contact-box">
      <div class="social">
        <p class="social-line"><span class="social-mark"></span>we.are.purelywindswept</p>
        <p class="social-line"><span class="social-mark"></span>_purelywindswept_</p>
      </div>
      <div class="contact-person">
        <p class="contact-name">Lorraine Pitt (Midlands):</p>
        <p class="contact-phone">
          <svg viewBox="0 0 24 24" aria-hidden="true"><path fill="#fff" d="M6.6 10.8c1.4 2.8 3.8 5.1 6.6 6.6l2.2-2.2c.3-.3.7-.4 1-.2 1.1.4 2.3.6 3.6.6.6 0 1 .4 1 1V20c0 .6-.4 1-1 1C10.6 21 3 13.4 3 4c0-.6.4-1 1-1h3.5c.6 0 1 .4 1 1 0 1.3.2 2.5.6 3.6.1.3 0 .7-.2 1z"/></svg>
          07700 452 183
        </p>
      </div>
      <div class="contact-person">
        <p class="contact-name">Tessa Orchard (South):</p>
        <p class="contact-phone">
          <svg viewBox="0 0 24 24" aria-hidden="true"><path fill="#fff" d="M6.6 10.8c1.4 2.8 3.8 5.1 6.6 6.6l2.2-2.2c.3-.3.7-.4 1-.2 1.1.4 2.3.6 3.6.6.6 0 1 .4 1 1V20c0 .6-.4 1-1 1C10.6 21 3 13.4 3 4c0-.6.4-1 1-1h3.5c.6 0 1 .4 1 1 0 1.3.2 2.5.6 3.6.1.3 0 .7-.2 1z"/></svg>
          07700 318 527
        </p>
      </div>
    </footer>
  </main>
</body>
</html>
```